A landing page for an exclusive club VELMONTA

We need a fresh, stylish and luxury design for a landing page of an international private club called VELMONTA.

After receiving your first drafts, let me briefly emphasize some important points:
1) Top picture: I would like to see here some good looking intelligent people (not dancing teenagers or smiling couple – because it’s not a pure dating website)
2) Member’s section: the main message of this slide is to communicate the idea of EXCLUSIVITY - the club has exclusive audience (well-educated, intellectual, financially successful people from world-leading universities and well-known companies). I do not want to reveal real members’ profiles on this slide (it’s allowed only in the review section)
3) Event section should not have real future events, just describe event categories.
4) Technology section should communicate the idea of sending REAL presents (a drink or flowers) to a girl via the app. (maybe by using some dynamic elements during the scrolling)
5) Review section – please make it individual design, not a standard one. Please add company’s names and job titles to reviewers.
6) Event section: we will not post actual events, rather some event categories with large attractive pictures.
7) Technical note: We do not have “register” button – people can log in or register only via QX – it’s one button
Let me know if you have any questions. Thank you for participating!

Kind regards,
Teodor Karvash

Reason: Dear designers, I have to extend the deadline as I did not receive any 5* designs so far. I would like to get a unique design - not a combination of standard blocks for landing pages. I understand the task is difficult, so I decided to give you more time to prepare well-though and original piece of art. Please use the text from the brief and add your ideas. The 3 main messages to communicate are: 1) Member’s section: the main message of this slide is to communicate the idea of EXCLUSIVITY - the club has exclusive audience (well-educated, intellectual, successful people from world-leading universities and well-known companies). I do not want to reveal real members’ profiles on this slide (it’s allowed only in the review section). 2) Event section: the club runs lots of invitation-only events in most exclusive venues. We will not post actual events, but rather some event categories with large attractive pictures and short descriptions. 3) Technology section should communicate the idea of sending REAL presents (a drink or flowers) to a girl via the app. If you can show it by using some dynamic elements during the scrolling it's fantastic! Good luck! I look forward for your creative ideas and art! Kind regards, Teodor Karvash

Target Market(s)

Alumni of top universities, middle- and top-level managers of large companies, financial professionals (investment bankers), successful entrepreneurs, recognized creative class (fashion designers, models).

Industry/Entity Type

Club

Coding

Coded - Design and coding required

Number of Pages Required

2 page

Font styles to use
Serif
Sans Serif
Other font styles liked:
• Lato, Oswald, Raleway

Requirements
Must have
• Adaptive design (desktop & mobile)
• Elegant and luxury design
• Structure according to the brief
Nice to have
• Dynamic elements/Layers on the landing page
Should not have
• Trivial stock photos.

```html
<!DOCTYPE html>
<html lang="en">
<head>
<meta charset="utf-8">
<title>Velmonta Social Discovery Club</title>
<link rel="stylesheet" href="https://fonts.googleapis.com/css2?family=Tinos:ital,wght@0,400;0,700;1,400&family=Lato:ital,wght@0,400;0,700;0,900;1,400&family=Montserrat:wght@400;600;700&display=swap">
<style>
:root{
  --gold:#d9a65a;
  --gold-soft:#e6b56a;
  --ink:#1f1f1f;
  --grey:#6f6f6f;
  --grey-light:#9a9a9a;
  --faint:#f0f0f0;
  --navy:#33508c;
  --footer:#2a2627;
  --footer-text:#a8a3a3;
  --white:#ffffff;
}
*{margin:0;padding:0;box-sizing:border-box}
html,body{width:1200px;height:3005px;overflow:hidden}
body{position:relative;background:var(--white);font-family:'Lato',sans-serif;color:var(--ink)}
.abs{position:absolute}

/* hero */
.hero{left:0;top:0;width:1200px;height:520px;
  background:linear-gradient(180deg,#6e5f78 0%,#8a6f7c 35%,#b78f80 60%,#cdbdb4 78%,#e9e2de 100%)}
.hero-shade{left:0;top:0;width:1200px;height:520px;background:linear-gradient(90deg,rgba(40,30,45,.35),rgba(0,0,0,0) 40%,rgba(0,0,0,0) 70%,rgba(255,255,255,.25))}
.brand{left:150px;top:20px;width:216px;display:flex;flex-direction:column;align-items:center;gap:10px}
.brand-dot{width:42px;height:42px;border:2px solid var(--white);border-radius:50%}
.brand-name{font-weight:400;font-size:15px;letter-spacing:8px;color:var(--white)}
.nav{left:562px;top:44px;display:flex;font-family:'Montserrat',sans-serif;font-size:10.5px;font-weight:600;letter-spacing:1px;color:var(--white)}
.nav a{color:inherit;text-decoration:none;margin-right:34px;position:relative}
.nav a.active{color:var(--gold-soft)}
.nav a.active::after{content:"";position:absolute;left:-6px;right:-6px;top:26px;height:2px;background:var(--gold-soft)}
.play{left:564px;top:224px}

.intro-card{left:156px;top:420px;width:886px;height:192px;background:#fdf9f8;box-shadow:0 18px 30px rgba(0,0,0,.18);text-align:center}
.intro-card h1{font-family:'Tinos',serif;font-weight:400;font-size:28px;color:#2b2b2b;margin-top:36px}
.intro-card p{font-size:12.5px;line-height:17px;color:var(--grey);width:660px;margin:6px auto 0}
.btn-login{display:inline-flex;align-items:center;gap:22px;margin-top:18px;background:var(--navy);color:var(--white);font-family:'Montserrat',sans-serif;font-weight:700;font-size:10px;letter-spacing:.8px;height:32px;padding:0 22px 0 20px}
.btn-login .sq{width:8px;height:8px;background:var(--white)}

/* members */
.member-mark{background:var(--faint)}
.mark-round{border-radius:50%}
.mark-pill{border-radius:20px}
.members{left:0;top:710px;width:1200px;text-align:center}
.members h2{font-family:'Tinos',serif;font-weight:400;font-size:36px;color:#1d1d1d}
.members p{width:470px;margin:12px auto 0;font-size:11.5px;line-height:16px;color:var(--grey)}
.btn-outline{display:inline-block;margin-top:26px;border:2px solid var(--gold);color:var(--gold);font-family:'Montserrat',sans-serif;font-weight:700;font-size:10px;letter-spacing:1px;padding:8px 18px}

.events-title{left:0;top:984px;width:1200px;text-align:center;font-family:'Tinos',serif;font-weight:400;font-size:29px;color:#1d1d1d}
.events{left:0;top:1062px;width:1200px;height:480px;display:grid;grid-template-columns:400px 400px 400px;grid-template-rows:240px 240px}
.event{position:relative;display:flex;flex-direction:column;align-items:center;justify-content:center;color:var(--white)}
.event h3{font-weight:400;font-size:19px;text-shadow:0 1px 3px rgba(0,0,0,.4)}
.event time{margin-top:5px;font-family:'Montserrat',sans-serif;font-weight:700;font-size:9.5px;letter-spacing:.4px}
.ph-lake{background:linear-gradient(160deg,#9fb5c7 0%,#7d8c86 40%,#8a6f4f 70%,#5b4a36 100%)}
.ph-city{background:linear-gradient(160deg,#d9c8b4 0%,#b7a48c 35%,#8f6f5a 65%,#5e4a3c 100%)}
.ph-bar{background:linear-gradient(160deg,#8b6a4c 0%,#6b4e38 40%,#d8b894 75%,#a07a58 100%)}
.ph-dark{background:linear-gradient(160deg,#3d3836 0%,#2d2827 50%,#4a3e36 100%)}
.frame{position:absolute;left:8px;top:8px;right:8px;bottom:8px;
  background:
   linear-gradient(#fff,#fff) left top/34px 2px no-repeat,
   linear-gradient(#fff,#fff) left top/2px 34px no-repeat,
   linear-gradient(#fff,#fff) right top/34px 2px no-repeat,
   linear-gradient(#fff,#fff) right top/2px 34px no-repeat,
   linear-gradient(#fff,#fff) left bottom/34px 2px no-repeat,
   linear-gradient(#fff,#fff) left bottom/2px 34px no-repeat,
   linear-gradient(#fff,#fff) right bottom/34px 2px no-repeat,
   linear-gradient(#fff,#fff) right bottom/2px 34px no-repeat}

/* newsletter */
.newsletter{left:0;top:1600px;width:1200px;text-align:center}
.newsletter h2{font-family:'Tinos',serif;font-weight:700;font-size:19px;color:#1d1d1d}
.newsletter p{font-size:10.5px;color:var(--grey);margin-top:4px}
.subscribe{left:384px;top:1662px;display:flex}
.subscribe .field{width:302px;height:32px;border:1px solid #e2e2e2;font-style:italic;font-size:10.5px;color:#aaa;padding:9px 14px}
.subscribe .send{width:128px;height:32px;background:var(--gold-soft);color:var(--white);font-family:'Montserrat',sans-serif;font-weight:700;font-size:10px;letter-spacing:1px;display:flex;align-items:center;justify-content:center;gap:8px}

/* technology */
.tech-band{left:0;top:1762px;width:1200px;height:440px;
  background:radial-gradient(ellipse 420px 300px at 830px 200px,#6c7378 0%,rgba(80,88,94,0) 70%),linear-gradient(100deg,#2e3a42 0%,#3f4a52 45%,#55606a 100%)}
.tech-phone{left:770px;top:1790px;width:190px;height:370px;border-radius:28px;
  background:linear-gradient(180deg,#eceef0 0%,#dfe2e5 100%);transform:rotate(14deg);box-shadow:0 20px 40px rgba(0,0,0,.35)}
.tech-phone-screen{left:786px;top:1846px;width:158px;height:262px;border-radius:4px;
  background:linear-gradient(180deg,#f7f7f8 0%,#f3eef0 55%,#e9c9cc 100%);transform:rotate(14deg);transform-origin:85px -30px}
.tech-title{left:156px;top:1894px;font-family:'Tinos',serif;font-weight:400;font-size:28px;color:var(--white)}
.tech-copy{left:156px;top:1934px;width:520px;font-size:13px;line-height:18px;color:#eef0f2}
.avail{left:156px;top:2010px;font-weight:700;font-size:12px;color:var(--white)}
.store{top:2040px;height:40px;display:flex;align-items:center;gap:10px;font-family:'Montserrat',sans-serif;font-weight:600;font-size:12.5px;color:var(--white);padding:0 20px}
.store-play{left:156px;width:150px;background:var(--gold-soft)}
.store-app{left:332px;width:134px;border:2px solid var(--white)}
.store .sq{width:12px;height:12px;background:var(--white)}

/* reviews */
.reviews-title{left:0;top:2256px;width:1200px;text-align:center;font-family:'Tinos',serif;font-weight:400;font-size:26px;color:#1d1d1d}
.quote{left:0;top:2402px;width:1200px;text-align:center}
.quote p{width:680px;margin:0 auto;font-style:italic;font-size:12px;line-height:16px;color:var(--grey-light)}
.avatar{border-radius:50%;background:linear-gradient(160deg,#d6d0cc,#a8a19c)}
.avatar.main{background:linear-gradient(160deg,#3a4452,#1f2630);border:3px solid #fff;box-shadow:0 0 0 1px #ddd}
.reviewer{left:0;top:2586px;width:1200px;text-align:center}
.reviewer strong{display:block;font-size:13.5px;color:#1d1d1d}
.reviewer span{font-size:11px;color:var(--grey-light)}

/* footer */
.footer{left:0;top:2680px;width:1200px;height:325px;background:var(--footer)}
.fcol{top:2740px;font-size:11px;line-height:19px;color:var(--footer-text);list-style:none}
.fcol .hl{color:var(--gold-soft)}
.fcol li{display:flex;align-items:center;gap:10px}
.ico{width:8px;height:8px;background:var(--footer-text);border-radius:2px}
.hl .ico{background:var(--gold-soft)}
.divider{left:130px;top:2908px;width:936px;height:1px;background:#3e3839}
.foot-brand{left:156px;top:2940px;display:flex;align-items:center;gap:14px;font-size:11px;color:var(--footer-text)}
.foot-brand .dot{width:32px;height:32px;border:2px solid var(--footer-text);border-radius:50%}
.to-top{left:1030px;top:2948px}
</style>
</head>
<body>

<!-- hero -->
<div class="abs hero" role="img" aria-label="Evening rooftop terrace over a city skyline with two elegantly dressed guests holding champagne"></div>
<div class="abs hero-shade"></div>
<div class="abs brand"><span class="brand-dot"></span><span class="brand-name">VELMONTA</span></div>
<nav class="abs nav">
  <a class="active">HOME</a><a>MEDIA</a><a>PARTNERS</a><a>FAQ'S</a><a>CONTACT</a><a>QX</a>
</nav>
<svg class="abs play" width="68" height="68" viewBox="0 0 68 68">
  <circle cx="34" cy="34" r="32" fill="none" stroke="#fff" stroke-width="2.5"/>
  <path d="M28 22 L46 34 L28 46 Z" fill="none" stroke="#fff" stroke-width="2.5" stroke-linejoin="round"/>
</svg>

<section class="abs intro-card">
  <h1>Velmonta Social Discovery Club</h1>
  <p>Velmonta Club is an international circle of trust which brings together exceptional people committed to building lasting relationship: personal or business.</p>
  <div class="btn-login"><span class="sq"></span>LOGIN WITH QX</div>
</section>

<!-- member partner badges -->
<div class="abs member-mark mark-pill" style="left:196px;top:700px;width:144px;height:30px"></div>
<div class="abs member-mark" style="left:206px;top:740px;width:118px;height:8px"></div>
<div class="abs member-mark mark-round" style="left:50px;top:806px;width:26px;height:26px"></div>
<div class="abs member-mark" style="left:86px;top:812px;width:130px;height:14px"></div>
<div class="abs member-mark" style="left:206px;top:876px;width:170px;height:12px"></div>
<div class="abs member-mark mark-pill" style="left:138px;top:946px;width:170px;height:24px"></div>
<div class="abs member-mark mark-round" style="left:900px;top:698px;width:40px;height:40px"></div>
<div class="abs member-mark" style="left:858px;top:746px;width:124px;height:10px"></div>
<div class="abs member-mark mark-pill" style="left:966px;top:816px;width:138px;height:30px"></div>
<div class="abs member-mark" style="left:766px;top:866px;width:90px;height:20px"></div>
<div class="abs member-mark mark-round" style="left:866px;top:864px;width:24px;height:24px"></div>
<div class="abs member-mark mark-round" style="left:862px;top:946px;width:26px;height:26px"></div>
<div class="abs member-mark" style="left:896px;top:952px;width:98px;height:16px"></div>
<section class="abs members">
  <h2>Our Members</h2>
  <p>Club membership is granted based on professional and personal accomplishments, education background, and a social profile of an applicant. Our carefully selected members come from world leading universities, top-tier companies and successful family businesses.</p>
  <span class="btn-outline">DISCOVER MORE</span>
</section>

<!-- events -->
<h2 class="abs events-title">Up coming events</h2>
<section class="abs events">
  <div class="event ph-lake" role="img" aria-label="Friends relaxing on a hillside above a lake and city"><h3>Black-tie Events</h3><time>&#9632; JUNE 24TH 2016</time></div>
  <div class="event ph-dark" role="img" aria-label="Friends at a bar table in dim evening light"><span class="frame"></span><h3>Quiz Nights</h3><time>&#9632; JUNE 24TH 2016</time></div>
  <div class="event ph-city" role="img" aria-label="Travellers reading a map in an old European square"><h3>Weekend Trips</h3><time>&#9632; JUNE 24TH 2016</time></div>
  <div class="event ph-city" role="img" aria-label="Travellers reading a map in an old European square"><h3>Theatre Nights</h3><time>&#9632; JUNE 24TH 2016</time></div>
  <div class="event ph-lake" role="img" aria-label="Friends relaxing on a hillside above a lake and city"><h3>Friday Parties</h3><time>&#9632; JUNE 24TH 2016</time></div>
  <div class="event ph-bar" role="img" aria-label="Friends raising glasses at a lunch table"><h3>Networking Lunches</h3><time>&#9632; JUNE 24TH 2016</time></div>
</section>

<!-- newsletter -->
<section class="abs newsletter">
  <h2>Sign Up for Our Newsletter</h2>
  <p>Velmonta Club Offers Daily Events for Members to Socialise, Network and Build Relationships</p>
</section>
<div class="abs subscribe">
  <div class="field">Enter your email ...</div>
  <div class="send">
    <svg width="11" height="11" viewBox="0 0 11 11"><path d="M0 5 L11 0 L7 11 L5 6 Z" fill="#fff"/></svg>SEND
  </div>
</div>

<!-- technology -->
<section class="abs tech-band" role="img" aria-label="Soft blurred background behind the mobile app"></section>
<div class="abs tech-phone" role="img" aria-label="Hand holding a smartphone showing the club chat with a gift of flowers"></div>
<div class="abs tech-phone-screen"></div>
<h2 class="abs tech-title">Our Powerfull Technology</h2>
<p class="abs tech-copy">Our state-of-the-art mobile app helps members get together, interact at events, discover people nearby and evenreceive real presents.</p>
<div class="abs avail">Available on the</div>
<div class="abs store store-play"><span class="sq"></span>Playdock</div>
<div class="abs store store-app"><span class="sq"></span>Appvault</div>

<!-- reviews -->
<h2 class="abs reviews-title">What our club members says?</h2>
<svg class="abs" style="left:572px;top:2330px" width="56" height="50" viewBox="0 0 56 50">
  <path d="M6 4 H34 a4 4 0 0 1 4 4 V26 a4 4 0 0 1 -4 4 H16 L8 38 V30 H6 a4 4 0 0 1 -4 -4 V8 a4 4 0 0 1 4 -4Z" fill="none" stroke="#cfcfcf" stroke-width="2"/>
  <path d="M42 16 H50 a4 4 0 0 1 4 4 V36 a4 4 0 0 1 -4 4 H48 V47 L41 40 H26 a4 4 0 0 1 -4 -4 V34" fill="none" stroke="#cfcfcf" stroke-width="2"/>
</svg>
<div class="abs quote"><p>Lorem Ipsum is simply dummy text of the printing and typesetting industry. Lorem Ipsum has been the industry's standard dummy text ever since the 1500s, when an unknown printer took a galley of type and scrambled it to make a type specimen book. It has survived not only five centuries, but also the leap into electronic typesetting, remaining essentially unchanged.</p></div>
<svg class="abs" style="left:398px;top:2518px" width="20" height="38" viewBox="0 0 20 38"><path d="M18 2 L3 19 L18 36" fill="none" stroke="#c9c9c9" stroke-width="2"/></svg>
<svg class="abs" style="left:780px;top:2518px" width="20" height="38" viewBox="0 0 20 38"><path d="M2 2 L17 19 L2 36" fill="none" stroke="#d9a65a" stroke-width="2"/></svg>
<div class="abs avatar" role="img" aria-label="Member portrait" style="left:494px;top:2510px;width:52px;height:52px"></div>
<div class="abs avatar main" role="img" aria-label="Member portrait" style="left:562px;top:2498px;width:76px;height:76px"></div>
<div class="abs avatar" role="img" aria-label="Member portrait" style="left:654px;top:2510px;width:52px;height:52px"></div>
<div class="abs reviewer"><strong>Marek Lindqvist</strong><span>- Project Manager at Northvale Partners -</span></div>

<!-- footer -->
<footer class="abs footer"></footer>
<ul class="abs fcol" style="left:156px"><li>About</li><li class="hl">Media</li><li>Partners</li><li>Our Location</li><li>Career</li><li>Contact</li></ul>
<ul class="abs fcol" style="left:384px"><li>Privileges</li><li>Unser Agreement</li><li>Confidentiality</li></ul>
<ul class="abs fcol" style="left:610px"><li>Sitemap</li><li>Tearm &amp; Condition</li><li>Privacy Policy</li><li>Help</li></ul>
<ul class="abs fcol" style="left:838px"><li class="hl"><span class="ico"></span>Chirpline</li><li><span class="ico"></span>QX</li><li><span class="ico"></span>Snapgrid</li><li><span class="ico"></span>Circlesphere</li><li><span class="ico"></span>Streamtube</li></ul>
<div class="abs divider"></div>
<div class="abs foot-brand"><span class="dot"></span>@ 2016 Velmonta. All Rights Reserved.</div>
<svg class="abs to-top" width="14" height="14" viewBox="0 0 14 14"><path d="M7 2 L12 8 H9 V12 H5 V8 H2 Z" fill="#e6b56a"/></svg>

</body>
</html>
```